Bellwyn Strategic

Business Development Consulting Firm

Target Market(s)

Federal Government, 8(a) companies, Small Businesses

Industry/Entity Type

Private Sector, US Government

Contact Information for Business Card

8(a) Program Capture, Business Development, Industry Trends & Analysis, Strategic Teaming, Cyber Solutions

Colors

Designer to choose colors to be used in the design.

```html
<!DOCTYPE html>
<html lang="en">
<head>
<meta charset="utf-8">
<title>Bellwyn Strategic — Business Card</title>
<link href="https://fonts.googleapis.com/css2?family=Montserrat:wght@600;700&family=Poppins:wght@400;500;600&display=swap" rel="stylesheet">
<style>
  :root {
    --backdrop: #8a8a8a;
    --navy: #004a7c;
    --blue: #0068b0;
    --white: #ffffff;
    --rule: #2a6fa6;
  }
  * { margin: 0; padding: 0; box-sizing: border-box; }
  html, body {
    width: 1093px; height: 1200px; overflow: hidden;
    background: var(--backdrop);
    font-family: "Poppins", sans-serif;
  }
  .card {
    position: absolute; left: 264px;
    width: 580px; height: 357px;
    border-radius: 24px; overflow: hidden;
  }
  .card--front { top: 226px; background: var(--navy); color: var(--white); }
  .card--back { top: 621px; background: var(--white); }

  .front__accent {
    position: absolute; right: -150px; top: 40px;
    width: 380px; height: 380px; border-radius: 50%;
    background: var(--blue);
  }
  .holder { position: absolute; left: 30px; top: 40px; }
  .holder__name {
    font-family: "Montserrat", sans-serif; font-weight: 700;
    font-size: 23px; letter-spacing: 0.2px; line-height: 1;
  }
  .holder__role { font-size: 17px; line-height: 1.2; margin-top: 2px; }
  .address {
    position: absolute; left: 27px; top: 154px;
    font-size: 17px; line-height: 21px;
  }
  .contacts {
    position: absolute; left: 30px; top: 259px;
    list-style: none; font-size: 17px; line-height: 21px;
  }
  .contacts li { display: flex; align-items: center; gap: 7px; }
  .contacts svg { width: 15px; height: 15px; flex: none; }

  .brand {
    position: absolute; left: 0; right: 0; top: 72px;
    display: flex; flex-direction: column; align-items: center;
  }
  .brand__dot {
    width: 84px; height: 84px; border-radius: 50%;
    background: var(--blue);
  }
  .brand__name {
    margin-top: 34px;
    font-family: "Poppins", sans-serif; font-weight: 600;
    font-size: 35px; letter-spacing: -0.5px; line-height: 1;
    color: var(--navy); text-transform: uppercase;
  }
  .web {
    position: absolute; left: 111px; right: 111px; top: 291px;
    display: flex; align-items: center; gap: 7px;
    font-size: 18px; color: var(--navy);
  }
  .web::before, .web::after {
    content: ""; flex: 1; height: 1px; background: var(--rule);
  }
</style>
</head>
<body>
  <section class="card card--front">
    <div class="front__accent" aria-hidden="true"></div>
    <div class="holder">
      <h1 class="holder__name">DANIEL WHITMORE</h1>
      <p class="holder__role">Managing Director</p>
    </div>
    <address class="address" style="font-style:normal">
      88, Harbor Ridge Avenue<br>20817, United States
    </address>
    <ul class="contacts">
      <li>
        <svg viewBox="0 0 16 16" aria-hidden="true"><path fill="none" stroke="#fff" stroke-width="1.6" d="M3.5 1.5l2.5 3-1.5 1.7c.8 2 2.3 3.5 4.3 4.3L10.5 9l3 2.5-1.3 2.2c-5.5-.3-9.6-4.4-9.9-9.9z"/><path fill="none" stroke="#fff" stroke-width="1.2" d="M9.5 2.5a4 4 0 0 1 4 4M9.5 4.8a1.8 1.8 0 0 1 1.7 1.7"/></svg>
        044-987 654 321
      </li>
      <li>
        <svg viewBox="0 0 16 16" aria-hidden="true"><rect x="1" y="3" width="14" height="10" fill="#fff"/><path d="M1 3l7 6 7-6M1 13l5-5M15 13l-5-5" fill="none" stroke="#004a7c" stroke-width="1.2"/></svg>
        hello@bellwyn.co
      </li>
      <li>
        <svg viewBox="0 0 16 16" aria-hidden="true"><g fill="none" stroke="#fff" stroke-width="1.3"><circle cx="8" cy="8" r="6.6"/><ellipse cx="8" cy="8" rx="3" ry="6.6"/><path d="M1.4 8h13.2M2.4 4.8h11.2M2.4 11.2h11.2"/></g></svg>
        www.bellwyn.co
      </li>
    </ul>
  </section>

  <section class="card card--back">
    <div class="brand">
      <div class="brand__dot" aria-hidden="true"></div>
      <h2 class="brand__name">Bellwyn Strategic</h2>
    </div>
    <p class="web">www.bellwyn.co</p>
  </section>
</body>
</html>
```